Marlow Sky Charter E-mail Signature

Need to create an email signature for Marlow Sky Charter. Signature should include the Marlow logo and the associated QFTR member logo

```html
<!DOCTYPE html>
<html lang="en">
<head>
<meta charset="utf-8">
<title>Marlow Sky Charter – Email Signature</title>
<link rel="stylesheet" href="https://fonts.googleapis.com/css2?family=Nunito:wght@400;600;700&display=swap">
<style>
  :root {
    --page-bg: #9a9a9a;
    --paper: #ffffff;
    --brand-blue: #2767b2;
    --ink: #3c3c3c;
    --on-blue: #ffffff;
  }
  * { margin: 0; padding: 0; box-sizing: border-box; }
  html, body {
    width: 1200px;
    height: 1200px;
    overflow: hidden;
    background: var(--page-bg);
    font-family: "Nunito", sans-serif;
  }
  .signature {
    position: absolute;
    left: 94px;
    top: 431px;
    width: 1012px;
    height: 337px;
    background: var(--paper);
  }
  .signature__top {
    position: absolute;
    left: 0; top: 0;
    width: 100%;
    height: 169px;
  }
  .person {
    position: absolute;
    left: 56px;
    top: 56px;
  }
  .person__name {
    font-size: 36px;
    font-weight: 600;
    line-height: 1;
    color: var(--brand-blue);
    letter-spacing: 0.5px;
  }
  .person__role {
    margin-top: 8px;
    font-size: 19px;
    font-weight: 400;
    color: var(--ink);
  }
  .brand {
    position: absolute;
    right: 88px;
    top: 62px;
    font-size: 40px;
    font-weight: 700;
    color: var(--brand-blue);
    letter-spacing: 0.5px;
    white-space: nowrap;
  }
  .signature__band {
    position: absolute;
    left: 0; top: 169px;
    width: 100%;
    height: 168px;
    background: var(--brand-blue);
    color: var(--on-blue);
  }
  .address {
    position: absolute;
    left: 56px;
    top: 44px;
    font-size: 18px;
    line-height: 25.5px;
    list-style: none;
  }
  .contact {
    position: absolute;
    left: 239px;
    top: 42px;
    list-style: none;
    font-size: 18px;
    line-height: 26px;
  }
  .contact__item {
    display: flex;
    align-items: center;
    gap: 13px;
  }
  .contact__icon {
    width: 17px;
    height: 17px;
    flex: none;
  }
  .membership {
    position: absolute;
    left: 774px;
    top: 72px;
    display: flex;
    align-items: flex-end;
    gap: 11px;
  }
  .membership__mark {
    width: 44px;
    height: 32px;
    border-radius: 50%;
    background: var(--on-blue);
  }
  .membership__label {
    display: block;
    font-size: 11px;
    font-weight: 400;
    line-height: 1;
    margin-bottom: 4px;
  }
  .membership__name {
    display: block;
    font-size: 28px;
    font-weight: 600;
    line-height: 1;
    letter-spacing: 3px;
  }
</style>
</head>
<body>
  <section class="signature" aria-label="Email signature">
    <header class="signature__top">
      <div class="person">
        <p class="person__name">DANA WHITFIELD</p>
        <p class="person__role">Operational Manager</p>
      </div>
      <p class="brand">Marlow Sky Charter</p>
    </header>

    <footer class="signature__band">
      <ul class="address">
        <li>412 W Harbor Lane</li>
        <li>Suite 210</li>
        <li>Aurora, IL 60505</li>
      </ul>

      <ul class="contact">
        <li class="contact__item">
          <svg class="contact__icon" viewBox="0 0 24 24" aria-hidden="true">
            <path fill="#fff" d="M6.6 10.8a15.2 15.2 0 0 0 6.6 6.6l2.2-2.2c.3-.3.7-.4 1-.2 1.1.4 2.3.6 3.6.6.6 0 1 .4 1 1V20c0 .6-.4 1-1 1A17 17 0 0 1 3 4c0-.6.4-1 1-1h3.5c.6 0 1 .4 1 1 0 1.3.2 2.5.6 3.6.1.3 0 .7-.2 1z"/>
          </svg>
          <span>555-204-3187</span>
        </li>
        <li class="contact__item">
          <svg class="contact__icon" viewBox="0 0 24 24" aria-hidden="true">
            <rect x="2" y="5" width="20" height="14" rx="2" fill="#fff"/>
            <path d="M3 6.5l9 6.5 9-6.5" fill="none" stroke="#2767b2" stroke-width="2"/>
          </svg>
          <span>info@marlowskymail.com</span>
        </li>
        <li class="contact__item">
          <svg class="contact__icon" viewBox="0 0 24 24" aria-hidden="true">
            <g fill="none" stroke="#fff" stroke-width="1.5">
              <circle cx="12" cy="12" r="9.5"/>
              <ellipse cx="12" cy="12" rx="4.5" ry="9.5"/>
              <path d="M2.5 12h19M4 7h16M4 17h16M12 2.5v19"/>
            </g>
          </svg>
          <span>marlowskymail.com</span>
        </li>
      </ul>

      <div class="membership">
        <span class="membership__mark" aria-hidden="true"></span>
        <div>
          <span class="membership__label">member of</span>
          <span class="membership__name">QFTR</span>
        </div>
      </div>
    </footer>
  </section>
</body>
</html>
```